Flyer for Azienda Agricola Valtorna Wine producer

We need a flyer with the most important information about us. The structure of the flyer will be similar to the sample attached to this request.
We are a new producer of wine, In the Langhe region (Piemonte, Italy). We produce a small quantity of high quality wine. Our wines are Moscato d'Asti DOCG and Vermouth Bianco di Moscato d'Asti. From the next year we'll start to sell also 2 types of sparkling wine, one white and second rosè.
Our sales strategy is oriented to B2C thanks to our e-commerce web site and to other web opportunity (www.aziendaagricolavaltorna.it).
In the attached file the labels of our wines, they can show the graphic still that we use since now, in particular we always use the leaf of grapes.
In case it can be usefull and in the flyer will be enough space, we can provide some others photo of ours grapes and panorama.
Thank in advance for your proposal
Carlo

```html
<!DOCTYPE html>
<html lang="it">
<head>
<meta charset="utf-8">
<title>Azienda Agricola Valtorna – Pieghevole</title>
<link href="https://fonts.googleapis.com/css2?family=Jost:wght@400;500;600&display=swap" rel="stylesheet">
<style>
  :root{
    --bg:#e4e4e4;
    --paper:#f4f5f3;
    --ink:#2b2b2b;
    --sky-top:#3a78bd;
    --sky-bottom:#8fb8de;
    --green:#4cb02e;
    --green-dark:#2f7d1e;
    --green-light:#8fd46a;
    --table:#5cbf3a;
    --table-alt:#6fcb4c;
  }
  *{box-sizing:border-box;margin:0;padding:0}
  html,body{width:1200px;height:800px;overflow:hidden;background:var(--bg)}
  body{font-family:"Jost",sans-serif;color:var(--ink)}
  .brochure{position:absolute;left:30px;top:20px;width:1140px;height:760px;display:flex;box-shadow:0 6px 22px rgba(0,0,0,.18)}
  .panel{position:relative;width:380px;height:760px;overflow:hidden;background:var(--paper)}
  .panel + .panel{border-left:1px solid rgba(0,0,0,.06)}
  .photo{position:absolute;left:0;width:100%}
  .bands{position:absolute;inset:0;width:100%;height:100%}
  .sky{position:absolute;left:0;top:0;width:100%;background:linear-gradient(180deg,var(--sky-top),var(--sky-bottom))}

  /* left panel */
  .territory{position:absolute;left:26px;top:54px;width:328px;color:#fff;font-size:12.5px;line-height:1.45}
  .story{position:absolute;left:26px;top:268px;width:328px;font-size:11.6px;line-height:1.42}
  .price-table{position:absolute;left:22px;width:336px;border-collapse:collapse;font-size:9.6px;color:#fff;background:var(--table)}
  .price-table caption{caption-side:top;background:var(--table);color:#fff;font-weight:600;font-size:10.5px;padding:4px 0 0;text-align:center}
  .price-table th{font-weight:600;padding:3px 2px;line-height:1.1;background:var(--green)}
  .price-table td{text-align:center;padding:2.2px 2px}
  .price-table tbody tr:nth-child(even){background:var(--table-alt)}
  .table-vermouth{top:432px}
  .table-moscato{top:560px}

  /* middle panel */
  .quote{position:absolute;left:24px;top:22px;width:332px;color:#fff;font-size:10.8px;line-height:1.4}
  .quote cite{display:block;font-style:normal;margin-top:2px}
  .contact{position:absolute;left:0;top:392px;width:100%;text-align:center;font-size:13px;line-height:1.35}
  .contact .icon{display:block;margin:6px auto 2px;width:16px;height:16px}
  .contact .strong{font-weight:600;font-size:14px}

  /* right panel */
  .brand{position:absolute;left:0;top:520px;width:100%;text-align:center}
  .brand-name{display:inline-flex;align-items:center;gap:10px;font-size:40px;font-weight:500;color:var(--green-dark)}
  .brand-name .dot{width:14px;height:14px;border-radius:50%;background:var(--green)}
  .brand-sub{display:block;font-size:15px;font-weight:500;color:var(--green-dark);letter-spacing:1px;margin-top:-2px}
  .web-pill{position:absolute;left:24px;top:626px;width:332px;height:30px;border-radius:15px;background:var(--green);color:#fff;font-size:14px;display:flex;align-items:center;justify-content:center}
</style>
</head>
<body>
<main class="brochure">

  <!-- Panel 1: territorio e listino -->
  <section class="panel panel-territory">
    <div class="sky" style="height:270px" role="img" aria-label="Cielo azzurro sopra le colline"></div>
    <div class="photo" style="top:230px;height:460px;background:linear-gradient(160deg,#e9e9ec,#c9c6d3 45%,#eef0ee)" role="img" aria-label="Grappolo d'uva scura sfumato"></div>
    <div class="photo" style="top:660px;height:100px;background:linear-gradient(90deg,#4a5a2a,#7b8a3e 40%,#c24a2a 55%,#5a6a30)" role="img" aria-label="Cassetta di uva bianca vendemmiata nella vigna"></div>
    <svg class="bands" viewBox="0 0 380 760" preserveAspectRatio="none" aria-hidden="true">
      <path d="M0 252 C110 200 250 200 380 232 L380 248 C250 218 110 220 0 268 Z" fill="var(--green-dark)"/>
      <path d="M0 262 C110 214 250 214 380 244 L380 260 C250 232 110 236 0 280 Z" fill="var(--green)"/>
      <path d="M0 700 C120 650 260 648 380 678 L380 690 C260 664 120 668 0 714 Z" fill="var(--green)"/>
    </svg>
    <p class="territory">Il territorio in cui si trova è quello del Comune di Borgo Collina, oggi riconosciuto come patrimonio dell’Unesco per la bellezza del territorio e per la maestria dei piemontesi che hanno saputo fare la storia del vino e produrne alcuni dei migliori al mondo.</p>
    <p class="story">L’Azienda nasce dalla passione per la terra e per i suoi prodotti, con l’esperienza maturata in decenni produce i suoi vini partendo dalle migliori uve della sua terra. Il nome dell’etichetta, Testa Bianca, nasce da come gli abitanti delle colline vicine chiamano la collina di Valtorna, perché, verso la fine dell’inverno guardando la collina di Valtorna si vede la cima ancora innevata mentre tutto intorno la primavera esplode, questa particolare caratteristica è data dall’esposizione a Nord Ovest della sua cima.</p>

    <table class="price-table table-vermouth">
      <caption>Vermouth Bianco Testa Bianca</caption>
      <thead><tr><th>Bottiglie</th><th>Costo imponibile</th><th>Sconto volume</th><th>Offerta imponibile</th><th>Vantaggio</th></tr></thead>
      <tbody>
        <tr><td>1</td><td>13,00</td><td></td><td>13,00</td><td></td></tr>
        <tr><td>6</td><td>78,00</td><td>2,5%</td><td>76,05</td><td>1,95</td></tr>
        <tr><td>12</td><td>156,00</td><td>5,0%</td><td>148,20</td><td>7,80</td></tr>
        <tr><td>18</td><td>234,00</td><td>7,5%</td><td>216,45</td><td>17,55</td></tr>
        <tr><td>24</td><td>312,00</td><td>10,0%</td><td>280,80</td><td>31,20</td></tr>
        <tr><td>36</td><td>468,00</td><td>12,5%</td><td>409,50</td><td>58,50</td></tr>
        <tr><td>48</td><td>624,00</td><td>15,0%</td><td>530,40</td><td>93,60</td></tr>
      </tbody>
    </table>

    <table class="price-table table-moscato">
      <caption>Moscato d’Asti DOCG Testa Bianca</caption>
      <thead><tr><th>Bottiglie</th><th>Costo imponibile</th><th>Sconto volume</th><th>Offerta imponibile</th><th>Vantaggio</th></tr></thead>
      <tbody>
        <tr><td>1</td><td>5,75</td><td></td><td>5,75</td><td></td></tr>
        <tr><td>6</td><td>34,50</td><td>2,5%</td><td>33,64</td><td>0,86</td></tr>
        <tr><td>12</td><td>69,00</td><td>5,0%</td><td>65,55</td><td>3,45</td></tr>
        <tr><td>18</td><td>103,50</td><td>7,5%</td><td>95,74</td><td>7,76</td></tr>
        <tr><td>24</td><td>138,00</td><td>10,0%</td><td>124,20</td><td>13,80</td></tr>
        <tr><td>36</td><td>207,00</td><td>12,5%</td><td>181,13</td><td>25,88</td></tr>
        <tr><td>48</td><td>276,00</td><td>15,0%</td><td>234,60</td><td>41,40</td></tr>
      </tbody>
    </table>
  </section>

  <!-- Panel 2: citazione e contatti -->
  <section class="panel panel-contact">
    <div class="sky" style="height:160px"></div>
    <div class="photo" style="top:120px;height:250px;background:linear-gradient(180deg,#7fa7cf 0%,#4f7d3a 22%,#3f6e2a 60%,#5b8c3a)" role="img" aria-label="Filari di vigna sotto il cielo azzurro"></div>
    <div class="photo" style="top:330px;height:370px;background:linear-gradient(180deg,#e8ebe6,#f1f2ef 40%,#dfe6dc)" role="img" aria-label="Vigna sfumata sullo sfondo"></div>
    <div class="photo" style="top:680px;height:80px;background:linear-gradient(90deg,#3f6a24,#6a8f3a,#3e5f22)" role="img" aria-label="Filari di vigna"></div>
    <svg class="bands" viewBox="0 0 380 760" preserveAspectRatio="none" aria-hidden="true">
      <path d="M0 322 C120 330 260 392 380 392 L380 408 C260 408 120 348 0 338 Z" fill="var(--green-dark)"/>
      <path d="M0 334 C120 344 260 404 380 404 L380 420 C260 420 120 362 0 352 Z" fill="var(--green)"/>
      <path d="M0 670 C120 696 250 706 380 698 L380 710 C250 718 120 710 0 684 Z" fill="var(--green)"/>
    </svg>
    <blockquote class="quote">“Traversai il torrente, sulla passerella, e mentre andavo pensavo che non c’è niente di più bello di una vigna ben curata, ben legata con le foglie giuste e quell’odore della terra scaldata dal sole d’agosto. Una vigna ben lavorata è come un corpo sano, che vive, che ha il suo respiro e il suo sudore.”<br>“A Borgo Collina entrai per un lungo viale che ai miei tempi non c’era, ma sentii subito l’odore, quella punta di vinacce, di mosto del Torna, di Vermouth.”
      <cite>(Elio Marrasco – Le vigne del Torna)</cite>
    </blockquote>
    <address class="contact" style="font-style:normal">
      <svg class="icon" viewBox="0 0 16 16" aria-hidden="true"><path d="M8 1a5 5 0 0 0-5 5c0 4 5 9 5 9s5-5 5-9a5 5 0 0 0-5-5zm0 7a2 2 0 1 1 0-4 2 2 0 0 1 0 4z" fill="var(--green)"/></svg>
      Azienda Agricola Valtorna<br>Località Valtorna, 14<br>12050 Borgo Collina CN Italia<br>Partita IVA: 01234567890
      <svg class="icon" viewBox="0 0 16 16" aria-hidden="true"><rect x="1.5" y="3.5" width="13" height="9" fill="none" stroke="var(--green)" stroke-width="1.4"/><path d="M1.5 3.5 8 9l6.5-5.5" fill="none" stroke="var(--green)" stroke-width="1.4"/></svg>
      info@valtorna.it
      <svg class="icon" viewBox="0 0 16 16" aria-hidden="true"><path d="M4 1.5h3l1 3-2 1.3a8 8 0 0 0 4.2 4.2L11.5 8l3 1v3c0 1-1 2-2 2A11 11 0 0 1 2 3.5c0-1 1-2 2-2z" fill="var(--green)"/></svg>
      <span class="strong">0141/555012 – 02/55501234</span>
      <svg class="icon" viewBox="0 0 16 16" aria-hidden="true"><rect x="4.5" y="1" width="7" height="14" rx="1.5" fill="none" stroke="var(--green)" stroke-width="1.4"/><circle cx="8" cy="12.5" r=".9" fill="var(--green)"/></svg>
      <span class="strong">333/5550147 – 345/5550198</span>
      <svg class="icon" viewBox="0 0 16 16" aria-hidden="true"><circle cx="8" cy="8" r="6.5" fill="none" stroke="var(--green)" stroke-width="1.4"/><path d="M1.5 8h13M8 1.5c-3 3.5-3 9.5 0 13M8 1.5c3 3.5 3 9.5 0 13" fill="none" stroke="var(--green)" stroke-width="1.1"/></svg>
      www.aziendaagricolavaltorna.it
    </address>
  </section>

  <!-- Panel 3: copertina -->
  <section class="panel panel-cover">
    <div class="photo" style="top:0;height:470px;background:radial-gradient(ellipse at 45% 35%,#b6d86a 0%,#6fa83a 35%,#2f5a1e 80%)" role="img" aria-label="Grappolo di uva bianca moscato sulla vite"></div>
    <svg class="bands" viewBox="0 0 380 760" preserveAspectRatio="none" aria-hidden="true">
      <path d="M0 420 C120 470 260 470 380 410 L380 760 L0 760 Z" fill="var(--paper)"/>
      <path d="M0 404 C120 456 260 456 380 394 L380 410 C260 472 120 472 0 420 Z" fill="var(--green-dark)"/>
      <path d="M0 414 C120 466 260 466 380 404 L380 420 C260 482 120 482 0 430 Z" fill="var(--green)"/>
    </svg>
    <div class="brand">
      <span class="brand-name"><span class="dot"></span>Valtorna</span>
      <span class="brand-sub">AZIENDA AGRICOLA</span>
    </div>
    <div class="web-pill">www.aziendaagricolavaltorna.it</div>
  </section>

</main>
</body>
</html>
```